Skin Brightening Poster Design Project

Poster design to promote skin brightening treatments during winter months.

Requirements
Must have
• Poster must be eye catching to both males and females.

List of services: IPL, Laser, Microdermabrasion, Peels

Dr. Welsford's Radiance Cream now available

Free consultations

Clinic details:
CBD: Suite 304, 7 Farrow Street Melbourne 9718 2043
Richmond: 415 Garnet Street Richmond 9386 5172
Dandenong: Shop 9 The Lantern Mall, Dandenong 9541 7630

Web site: www.dermalivo.com.au

A1 size poster
Should not have
• Poster design should not be similar to day spas, hairdressers or beauty salons

```html
<!DOCTYPE html>
<html lang="en">
<head>
<meta charset="utf-8">
<title>Skin Brightening Poster</title>
<link rel="stylesheet" href="https://fonts.googleapis.com/css2?family=Raleway:wght@300;400&family=Oswald:wght@500&family=PT+Serif:wght@400;700&display=swap">
<style>
  :root {
    --paper: #ffffff;
    --ink: #333333;
    --ink-soft: #4a4a4a;
    --pink: #c9557a;
    --pink-light: #e7a3b9;
    --skin-warm: #e9d3c8;
    --skin-light: #f5ebe5;
  }
  html, body {
    margin: 0;
    padding: 0;
    overflow: hidden;
    background: var(--paper);
  }
  .poster {
    position: relative;
    width: 847px;
    height: 1200px;
    overflow: hidden;
    background: var(--paper);
    color: var(--ink);
  }
  .hero-photo {
    position: absolute;
    left: 0;
    top: 0;
    width: 847px;
    height: 720px;
    background:
      radial-gradient(ellipse 60% 55% at 55% 40%, var(--skin-light) 0%, var(--skin-warm) 45%, rgba(233, 211, 200, 0) 80%),
      linear-gradient(180deg, #d9c1b6 0%, #efe2dc 55%, var(--paper) 100%);
  }
  .headline {
    position: absolute;
    left: 40px;
    top: 705px;
    margin: 0;
    font-family: "Raleway", sans-serif;
    font-weight: 300;
    color: var(--ink);
    line-height: 1;
  }
  .headline-main {
    display: block;
    font-size: 92px;
    letter-spacing: 18px;
  }
  .headline-sub {
    display: block;
    margin-top: 4px;
    font-size: 48px;
    font-weight: 400;
    letter-spacing: 9px;
  }
  .services {
    position: absolute;
    left: 42px;
    top: 862px;
    margin: 0;
    font-family: "Oswald", sans-serif;
    font-weight: 500;
    font-size: 40px;
    letter-spacing: 0.5px;
    color: var(--ink);
  }
  .offer-band {
    position: absolute;
    left: 28px;
    top: 930px;
    width: 819px;
    height: 60px;
    background: linear-gradient(90deg, var(--pink) 0%, #d7739a 55%, var(--pink-light) 100%);
  }
  .offer-band p {
    margin: 0;
    padding-left: 14px;
    line-height: 60px;
    font-family: "Raleway", sans-serif;
    font-weight: 400;
    font-size: 25px;
    letter-spacing: 0.5px;
    color: var(--paper);
    text-transform: uppercase;
  }
  .free-consult {
    position: absolute;
    left: 42px;
    top: 994px;
    margin: 0;
    font-family: "Oswald", sans-serif;
    font-weight: 500;
    font-size: 40px;
    color: var(--pink);
    text-transform: uppercase;
  }
  .clinics {
    position: absolute;
    left: 42px;
    top: 1066px;
    margin: 0;
    padding: 0;
    list-style: none;
    font-family: "PT Serif", serif;
    font-size: 20px;
    line-height: 33px;
    color: var(--ink-soft);
  }
  .clinics strong { color: var(--ink); }
  .website {
    position: absolute;
    left: 42px;
    top: 1162px;
    margin: 0;
    font-family: "PT Serif", serif;
    font-weight: 700;
    font-size: 20px;
    color: var(--ink);
  }
  .partner {
    position: absolute;
    right: 40px;
    top: 1080px;
    width: 150px;
    display: flex;
    align-items: center;
    gap: 8px;
  }
  .partner-mark {
    width: 26px;
    height: 26px;
    flex: none;
    border-radius: 50%;
    background: var(--pink);
  }
  .partner-name {
    margin: 0;
    font-family: "PT Serif", serif;
    font-size: 13px;
    line-height: 15px;
    color: var(--ink-soft);
  }
</style>
</head>
<body>
  <main class="poster">
    <div class="hero-photo" role="img" aria-label="Close-up portrait photograph of a woman with bright, even skin fading into white"></div>

    <h1 class="headline">
      <span class="headline-main">SKIN</span>
      <span class="headline-sub">BRIGHTENING</span>
    </h1>

    <p class="services">IPL, LASER, MICRODERMABRASION, PEELS</p>

    <div class="offer-band">
      <p>Dr. Welsford's Radiance Cream now available!</p>
    </div>

    <p class="free-consult">Free consultations!</p>

    <ul class="clinics">
      <li><strong>CBD:</strong> Suite 304, 7 Farrow Street Melbourne 9718 2043</li>
      <li><strong>Richmond:</strong> 415 Garnet Street Richmond 9386 5172</li>
      <li><strong>Dandenong:</strong> Shop 9 The Lantern Mall, Dandenong 9541 7630</li>
    </ul>

    <p class="website">www.dermalivo.com.au</p>

    <div class="partner">
      <span class="partner-mark"></span>
      <p class="partner-name">Southbank Dermal Institute</p>
    </div>
  </main>
</body>
</html>
```